Album Jacket for young indie musicians in AFRICA #2 Baraka, Tumaini And Neema (Peace, Love And Unity)

We are ZEBO SOUND (zebo-sound.example), a music label for young African musicians living in a slum. I would like to ask you to design our new album's cover jacket. The title is Baraka, Tumaini And Neema (it means "Peace, Love And Unity" in Swahili. I entrust you whether you use English words in the design or not.), musician name is Daniel Okwaro. Add our label logo (we have various versions and can provide). I attached Daniel Okwaro's photo also. Please listen to the music of the album on Soundcloud. https://audiovault.example/tags/danielokwaro

Target Market(s)

International. not only African music funs.

Requirements
Must have
• Title, Musician's name, ZEBO SOUND Logo
• In order to upload to iTunes, I require the final that the following conditions are met.
• 1400 x 1400 pixels
• JPG file type
• 72 - 300dpi (300dpi is the best)
• Less than 25mb
• RGB color scheme (not CMYK)
Nice to have
• His music is something bright and little funny. Please express the tone of music in the design.
Should not have
• African traditional image

```html
<!DOCTYPE html>
<html lang="en">
<head>
<meta charset="utf-8">
<title>Baraka, Tumaini And Neema — Daniel Okwaro</title>
<link rel="stylesheet" href="https://fonts.googleapis.com/css2?family=Montserrat:wght@700;800;900&display=swap">
<style>
  :root {
    --lime: #b9d93c;
    --lime-light: #d3e95a;
    --lime-deep: #8fb52a;
    --leaf: #5f8f22;
    --magenta: #9b1466;
    --white: #ffffff;
    --ink: #222222;
    --sun: #ffee1a;
    --shade: rgba(40, 50, 20, 0.55);
  }
  html, body {
    margin: 0;
    padding: 0;
    width: 1200px;
    height: 1200px;
    overflow: hidden;
    background: var(--lime);
  }
  .cover {
    position: relative;
    width: 1200px;
    height: 1200px;
    overflow: hidden;
    font-family: "Montserrat", Arial, sans-serif;
    font-weight: 900;
  }
  .backdrop {
    position: absolute;
    inset: 0;
    background:
      radial-gradient(circle at 75% 20%, rgba(230, 200, 80, 0.45), transparent 40%),
      radial-gradient(circle at 20% 60%, var(--lime-light), transparent 55%),
      linear-gradient(160deg, var(--lime-light) 0%, var(--lime) 45%, var(--lime-deep) 100%);
  }
  .portrait {
    position: absolute;
    left: 286px;
    top: 324px;
    width: 576px;
    height: 576px;
    border-radius: 50%;
    background:
      radial-gradient(circle at 50% 70%, #2f3a1e 0%, #3f5a1f 30%, transparent 55%),
      radial-gradient(circle at 30% 30%, #7fe07a 0%, var(--leaf) 60%, #486d1a 100%);
    box-shadow: 0 0 0 6px rgba(255, 255, 180, 0.35);
  }
  .decor {
    position: absolute;
    inset: 0;
  }
  .title-line {
    position: absolute;
    left: 74px;
    top: 36px;
    margin: 0;
    font-size: 104px;
    font-weight: 900;
    line-height: 1;
    letter-spacing: -1px;
    white-space: nowrap;
  }
  .title-line .word-one { color: var(--magenta); }
  .title-line .word-two { color: var(--white); }
  .title-and {
    position: absolute;
    left: 54px;
    top: 180px;
    writing-mode: vertical-rl;
    font-size: 80px;
    line-height: 1;
    color: var(--ink);
    letter-spacing: 2px;
  }
  .title-stack {
    position: absolute;
    left: 44px;
    top: 396px;
    width: 128px;
    font-size: 124px;
    line-height: 116px;
    color: var(--sun);
    text-align: center;
  }
  .title-stack span { display: block; }
  .artist-rule {
    position: absolute;
    left: 1038px;
    top: 318px;
    width: 2px;
    height: 768px;
    background: var(--ink);
  }
  .artist-name {
    position: absolute;
    left: 1054px;
    top: 322px;
    writing-mode: vertical-rl;
    font-size: 76px;
    font-weight: 900;
    line-height: 1;
    color: var(--ink);
    letter-spacing: 0;
    white-space: nowrap;
    margin: 0;
  }
  .label {
    position: absolute;
    left: 290px;
    top: 1046px;
    display: flex;
    align-items: center;
    gap: 30px;
  }
  .label-dot {
    width: 84px;
    height: 84px;
    border-radius: 50%;
    background: var(--ink);
  }
  .label-name {
    font-size: 72px;
    line-height: 1;
    color: var(--ink);
    letter-spacing: -1px;
  }
  .label-tagline {
    position: absolute;
    left: 468px;
    top: 1126px;
    font-size: 28px;
    font-weight: 800;
    color: var(--ink);
    white-space: nowrap;
  }
</style>
</head>
<body>
  <main class="cover">
    <div class="backdrop" role="img" aria-label="Green-tinted photo of trees, a courtyard and a large orange and white umbrella"></div>

    <svg class="decor" width="1200" height="1200" viewBox="0 0 1200 1200" aria-hidden="true">
      <circle cx="282" cy="877" r="76" fill="var(--shade)"/>
      <circle cx="850" cy="390" r="30" fill="rgba(90, 40, 60, 0.5)"/>
      <circle cx="800" cy="405" r="22" fill="rgba(90, 40, 60, 0.45)"/>
      <circle cx="905" cy="335" r="11" fill="rgba(120, 30, 40, 0.6)"/>
      <circle cx="700" cy="480" r="60" fill="rgba(60, 50, 90, 0.35)"/>
    </svg>

    <div class="portrait" role="img" aria-label="Circular photo of the musician in a white shirt and dark waistcoat holding an umbrella"></div>

    <h1 class="title-line"><span class="word-one">BARAKA</span><span class="word-two">, TUMAINI</span></h1>
    <div class="title-and">AND</div>
    <div class="title-stack" aria-label="NEEMA">
      <span>N</span><span>E</span><span>E</span><span>M</span><span>A</span>
    </div>

    <div class="artist-rule"></div>
    <h2 class="artist-name">DANIEL OKWARO.</h2>

    <div class="label">
      <div class="label-dot"></div>
      <div class="label-name">ZEBO SOUND</div>
    </div>
    <div class="label-tagline">bright sounds for every ear</div>
  </main>
</body>
</html>
```